Corporate holiday party invitation

Please design a holiday party invitations that looks classy and festive for our member holiday party. The event is first class, semi-formal and needs to be conveyed as such. Please see file from last year so you can see what we are aiming for. The new wording for the invite is as follows: (please use similar fonts to the file provided)

BVK Dallas/Fort Worth
cordially invites you and a guest to the
Yearly Winter Guild Supper Soiree
on Thursday, December 16th
at 6:30pm in the evening

Merrow Tower, Lantern Club
4817 Pell Avenue, 40th floor
Dallas, TX 75288

Tickets are $100 per person and include:
open premium bar, appetizers, three course dinner
and entertainment

Holiday Cocktail Dress

Target Market(s)

middle aged corporate types

Industry/Entity Type

Event

Font styles to use
Script

Requirements
Must have
• Classy holiday feel and design elements,

```html
<!DOCTYPE html>
<html lang="en">
<head>
<meta charset="utf-8">
<title>Yearly Winter Guild Supper Soiree – Invitation</title>
<link rel="stylesheet" href="https://fonts.googleapis.com/css2?family=Parisienne&family=Montserrat:wght@500;600&display=swap">
<style>
  :root {
    --parchment: #f4e7c8;
    --parchment-edge: #e8d4a6;
    --gold: #c3923a;
    --gold-deep: #a87822;
    --gold-light: #e2bf72;
    --bloom: 222, 150, 72;
    --amber: #d98a1c;
    --script: #b98a2e;
  }
  * { margin: 0; padding: 0; box-sizing: border-box; }
  html, body { width: 849px; height: 1200px; overflow: hidden; background: var(--parchment); }
  .invitation {
    position: relative;
    width: 849px; height: 1200px;
    background: radial-gradient(ellipse at center, #f8eed6 0%, var(--parchment) 60%, var(--parchment-edge) 100%);
    font-family: "Montserrat", sans-serif;
  }
  .frame { position: absolute; border: 2px solid var(--gold); }
  .frame--outer { inset: 26px; }
  .frame--inner { inset: 38px; border-width: 1px; }

  .corner-ornament {
    position: absolute; width: 90px; height: 90px;
    background: radial-gradient(circle at 25% 25%, rgba(195,146,58,0.5), rgba(195,146,58,0) 68%);
  }
  .corner-ornament--tl { top: 30px; left: 30px; }
  .corner-ornament--tr { top: 30px; right: 30px; transform: scaleX(-1); }
  .corner-ornament--bl { bottom: 30px; left: 30px; transform: scaleY(-1); }
  .corner-ornament--br { bottom: 30px; right: 30px; transform: scale(-1,-1); }

  .floral-vine { position: absolute; width: 150px; }
  .floral-vine--left {
    left: 40px; top: 220px; height: 910px;
    background:
      radial-gradient(circle at 40px 40px, rgba(var(--bloom),0.55), rgba(var(--bloom),0) 40px),
      radial-gradient(circle at 90px 180px, rgba(var(--bloom),0.35), rgba(var(--bloom),0) 46px),
      radial-gradient(circle at 50px 340px, rgba(var(--bloom),0.45), rgba(var(--bloom),0) 55px),
      radial-gradient(circle at 100px 480px, rgba(var(--bloom),0.35), rgba(var(--bloom),0) 44px),
      radial-gradient(circle at 45px 620px, rgba(var(--bloom),0.45), rgba(var(--bloom),0) 58px),
      radial-gradient(circle at 95px 760px, rgba(var(--bloom),0.4), rgba(var(--bloom),0) 48px),
      radial-gradient(circle at 40px 860px, rgba(var(--bloom),0.4), rgba(var(--bloom),0) 50px);
  }
  .floral-vine--right {
    right: 40px; top: 200px; height: 900px;
    background:
      radial-gradient(circle at 100px 60px, rgba(var(--bloom),0.5), rgba(var(--bloom),0) 44px),
      radial-gradient(circle at 60px 200px, rgba(var(--bloom),0.35), rgba(var(--bloom),0) 46px),
      radial-gradient(circle at 105px 360px, rgba(var(--bloom),0.45), rgba(var(--bloom),0) 56px),
      radial-gradient(circle at 55px 500px, rgba(var(--bloom),0.35), rgba(var(--bloom),0) 44px),
      radial-gradient(circle at 100px 640px, rgba(var(--bloom),0.45), rgba(var(--bloom),0) 58px),
      radial-gradient(circle at 60px 790px, rgba(var(--bloom),0.4), rgba(var(--bloom),0) 48px),
      radial-gradient(circle at 110px 870px, rgba(var(--bloom),0.35), rgba(var(--bloom),0) 40px);
  }

  .divider-flourish {
    position: absolute; left: 50%; transform: translateX(-50%);
    width: 300px; height: 18px;
    background:
      radial-gradient(ellipse at center, var(--gold-deep) 0 9px, rgba(195,146,58,0) 10px),
      linear-gradient(90deg, rgba(195,146,58,0), var(--gold) 30%, var(--gold-light) 50%, var(--gold) 70%, rgba(195,146,58,0)) center / 100% 3px no-repeat;
  }
  .divider-flourish--top { top: 180px; }
  .divider-flourish--bottom { top: 428px; }

  .headline {
    position: absolute; top: 200px; left: 0; right: 0;
    text-align: center;
    font-family: "Parisienne", cursive; font-weight: 400;
    color: var(--script);
    font-size: 40px; line-height: 54px;
  }

  .details {
    position: absolute; left: 150px; right: 150px;
    text-align: center; color: var(--amber);
    text-transform: uppercase; font-weight: 600;
  }
  .details--when { top: 582px; font-size: 27px; line-height: 48px; }
  .details--where { top: 722px; font-size: 26px; line-height: 42px; }
  .details--tickets { top: 892px; font-size: 20px; line-height: 36px; font-weight: 500; }
  .rule {
    position: absolute; left: 190px; right: 190px;
    border-top: 2px dashed var(--gold-light);
  }
  .rule--one { top: 695px; }
  .rule--two { top: 866px; }

  .dress-code {
    position: absolute; top: 1060px; left: 204px; width: 441px; height: 42px;
    border: 2px dashed var(--gold);
    display: flex; align-items: center; justify-content: center;
    color: var(--gold-deep); font-size: 19px; font-weight: 600;
    letter-spacing: 4px; text-transform: uppercase;
  }
</style>
</head>
<body>
<main class="invitation">
  <div class="frame frame--outer"></div>
  <div class="frame frame--inner"></div>

  <div class="corner-ornament corner-ornament--tl" role="img" aria-label="Gold scrollwork corner ornament"></div>
  <div class="corner-ornament corner-ornament--tr" role="img" aria-label="Gold scrollwork corner ornament"></div>
  <div class="corner-ornament corner-ornament--bl" role="img" aria-label="Gold scrollwork corner ornament"></div>
  <div class="corner-ornament corner-ornament--br" role="img" aria-label="Gold scrollwork corner ornament"></div>

  <div class="floral-vine floral-vine--left" role="img" aria-label="Climbing golden floral vine with blossoms and swirls"></div>
  <div class="floral-vine floral-vine--right" role="img" aria-label="Climbing golden floral vine with blossoms and swirls"></div>

  <div class="divider-flourish divider-flourish--top" role="img" aria-label="Gold scroll flourish divider"></div>
  <h1 class="headline">
    BVK Dallas/Fort Worth<br>
    cordially invites you and a guest to the<br>
    Yearly Winter Guild<br>
    Supper Soiree
  </h1>
  <div class="divider-flourish divider-flourish--bottom" role="img" aria-label="Gold scroll flourish divider"></div>

  <p class="details details--when">On Thursday, December 16th<br>at 6:30pm in the evening</p>
  <div class="rule rule--one"></div>
  <p class="details details--where">Merrow Tower, Lantern Club<br>4817 Pell Avenue, 40th floor<br>Dallas, TX 75288</p>
  <div class="rule rule--two"></div>
  <p class="details details--tickets">Tickets are $100 per person and include:<br>open premium bar, appetizers,<br>three course dinner and entertainment</p>

  <div class="dress-code">Holiday Cocktail Dress</div>
</main>
</body>
</html>
```